Mirela Dawn Business Card Design

I need a business card for my daughter. She has it all described in the file below. But it needs to be square in shape. http://www.mireladawn.example is her web site

Target Market(s)

18-35 year old women

Industry/Entity Type

Fashion

Contact Information for Business Card

Please look at the attached file as it has all the details.

Requirements
Must have
• Please look at the attached file as it has all the details.
Nice to have
Should not have

```html
<!DOCTYPE html>
<html lang="en">
<head>
<meta charset="utf-8">
<title>Mirela Dawn — Business Card</title>
<link rel="stylesheet" href="https://fonts.googleapis.com/css2?family=Lora:wght@400;700&family=Kalam:wght@400&display=swap">
<style>
  :root {
    --backdrop: #5d6369;
    --card-edge: #0a0a0a;
    --rose: #c96b78;
    --rose-light: #e7b9c0;
    --ink: #111111;
    --paper: #ffffff;
    --leaf-deep: #1f4a5a;
    --leaf-mid: #3f7f86;
    --leaf-pale: #cfe3dd;
  }
  * { box-sizing: border-box; margin: 0; padding: 0; }
  html, body {
    width: 1200px; height: 1200px; overflow: hidden;
    background: var(--backdrop);
  }
  .canvas { position: relative; width: 1200px; height: 1200px; }

  .card {
    position: absolute; left: 330px; width: 540px; height: 540px;
    border: 9px solid var(--card-edge);
    overflow: hidden;
  }
  .card--front { top: 40px; }
  .card--back {
    top: 620px; background: var(--rose);
    display: flex; flex-direction: column;
    padding: 26px 0 34px 74px;
  }

  .foliage {
    position: absolute; inset: 0;
    background:
      radial-gradient(ellipse at 85% 10%, rgba(231,185,192,0.85) 0%, rgba(231,185,192,0) 35%),
      radial-gradient(ellipse at 20% 30%, var(--leaf-mid) 0%, rgba(63,127,134,0) 55%),
      radial-gradient(ellipse at 70% 75%, var(--leaf-deep) 0%, rgba(31,74,90,0) 60%),
      linear-gradient(135deg, var(--leaf-pale) 0%, var(--leaf-mid) 45%, var(--leaf-deep) 100%);
  }

  .nameplate {
    position: absolute; left: 50%; top: 50%;
    width: 250px; height: 204px; transform: translate(-50%, -50%);
    background: var(--rose);
    outline: 2px solid var(--paper); outline-offset: -2px;
    display: flex; flex-direction: column; align-items: center; justify-content: center;
    text-align: center;
  }
  .nameplate__name {
    font-family: "Lora", Georgia, serif; font-weight: 700;
    font-size: 28px; letter-spacing: 0.5px; color: var(--ink);
    text-transform: uppercase; white-space: nowrap;
  }
  .nameplate__rule { width: 200px; height: 1px; background: var(--paper); margin: 20px 0 18px; }
  .nameplate__motto {
    font-family: "Kalam", cursive; font-size: 24px; color: var(--ink);
  }

  .tagline {
    font-family: "Kalam", cursive; font-size: 21px; color: var(--paper);
    letter-spacing: 0.5px; white-space: nowrap;
  }

  .contact-list {
    list-style: none; margin-top: 58px;
    display: flex; flex-direction: column; gap: 27px;
  }
  .contact-list--links { margin-top: auto; gap: 22px; }

  .contact {
    display: flex; align-items: center; gap: 16px;
    font-family: "Lora", Georgia, serif; font-weight: 700; font-size: 21px;
    color: var(--ink); white-space: nowrap;
  }
  .contact--light { color: var(--paper); }
  .contact__dot { width: 34px; height: 34px; flex: none; display: block; }
  .contact__dot circle { fill: var(--ink); }
  .contact__dot path { fill: none; stroke: var(--paper); stroke-width: 2; stroke-linejoin: round; }
</style>
</head>
<body>
<main class="canvas">

  <section class="card card--front">
    <div class="foliage" role="img" aria-label="Photograph of tropical monstera leaves in teal and green with soft pink accents"></div>
    <div class="nameplate">
      <h1 class="nameplate__name">Mirela Dawn</h1>
      <div class="nameplate__rule"></div>
      <p class="nameplate__motto">fluent in fashion</p>
    </div>
  </section>

  <section class="card card--back">
    <p class="tagline">blogger &amp; vlogger// beauty-fashion-travel</p>

    <ul class="contact-list">
      <li class="contact">
        <svg class="contact__dot" viewBox="0 0 34 34"><circle cx="17" cy="17" r="17"/></svg>
        <span>snapgrid.example/mireladawnxo</span>
      </li>
      <li class="contact">
        <svg class="contact__dot" viewBox="0 0 34 34"><circle cx="17" cy="17" r="17"/></svg>
        <span>chirper.example/mireladawnxo</span>
      </li>
      <li class="contact">
        <svg class="contact__dot" viewBox="0 0 34 34"><circle cx="17" cy="17" r="17"/></svg>
        <span>@mireladawnxo</span>
      </li>
      <li class="contact">
        <svg class="contact__dot" viewBox="0 0 34 34"><circle cx="17" cy="17" r="17"/><path d="M9 11h16v12H9z M9 11l8 7 8-7"/></svg>
        <span>mirela@mireladawn.example</span>
      </li>
    </ul>

    <ul class="contact-list contact-list--links">
      <li class="contact contact--light">
        <svg class="contact__dot" viewBox="0 0 34 34"><circle cx="17" cy="17" r="17"/></svg>
        <span>vidcast.example/mireladawn</span>
      </li>
      <li class="contact contact--light">
        <svg class="contact__dot" viewBox="0 0 34 34"><circle cx="17" cy="17" r="17"/></svg>
        <span>mireladawn.example</span>
      </li>
    </ul>
  </section>

</main>
</body>
</html>
```